Interior designer's blog sharing design tips photos and design links

I need a fresh, fun, stylish blog design I love color and texture- I'm an interior designer in NY and want to come across as sophisticated yet approachable. I will be posting interior design photos and products

Target Market(s)

Women 25-54

Industry/Entity Type

Interior

Font styles to use
Serif

Colors
3377b5
886aae
ffc214
fbee3e
ec1f27
e54d9c
a54499

Requirements
Must have
• A space for my image. Link to my website. Pagebook. Snapgram and Chirper accoubts. Color cool fonts

```html
<!DOCTYPE html>
<html lang="en">
<head>
<meta charset="utf-8">
<title>Marlowe Interiors — Blog</title>
<link href="https://fonts.googleapis.com/css2?family=Lato:wght@400;700&family=Oswald:wght@500&display=swap" rel="stylesheet">
<style>
  :root{
    --ink:#2f2f2f;
    --body:#3c3c3c;
    --muted:#6e6e6e;
    --line:#e2e2e2;
    --panel-line:#dcdcdc;
    --red:#ec1f27;
    --pink:#e54d9c;
    --purple:#886aae;
    --green:#5bb32e;
    --header:#f1f0ee;
    --button-grey:#cfcfcf;
  }
  *{box-sizing:border-box;margin:0;padding:0}
  html,body{width:1200px;height:2365px;overflow:hidden}
  body{position:relative;background:#fff;font-family:"Lato",Arial,sans-serif;color:var(--body)}

  .site-header{position:absolute;left:0;top:0;width:1200px;height:58px;background:var(--header);box-shadow:0 1px 3px rgba(0,0,0,.12);z-index:2}
  .brand{position:absolute;left:173px;top:7px;font-family:"Oswald",Arial,sans-serif;font-weight:500;font-size:31px;color:var(--ink);letter-spacing:.3px}
  .social-links{position:absolute;left:906px;top:10px;display:flex;gap:5px}
  .social-links a{display:block;width:35px;height:35px;border-radius:50%;background:#2b2b2b}
  .social-links a:first-child{background:var(--red)}

  .hero{position:absolute;left:0;top:58px;width:1200px;height:469px;background:linear-gradient(160deg,#d9d2c6 0%,#f1ece4 30%,#bfae98 60%,#8f7a64 100%)}
  .avatar{position:absolute;left:800px;top:172px;width:205px;height:205px;border-radius:50%;border:5px solid #fff;background:radial-gradient(circle at 50% 40%,#d9b27c 0%,#8a6a52 55%,#3b2c2c 100%);box-shadow:0 2px 6px rgba(0,0,0,.25)}
  .profile-name{position:absolute;left:770px;top:400px;width:265px;text-align:center;font-size:24px;font-weight:700;color:#1d1d1d;letter-spacing:.5px}
  .profile-intro{position:absolute;left:786px;top:430px;width:233px;text-align:center;font-size:12.5px;line-height:17px;color:#1d1d1d}

  .post{position:absolute;left:172px;width:557px;border-bottom:1px solid var(--line);height:410px}
  .post:last-of-type{border-bottom:none}
  .post-title{font-size:27px;font-weight:400;color:var(--ink);line-height:32px}
  .post-sub{font-size:12.5px;color:#333;margin-top:1px}
  .post-image{display:block;width:557px;height:186px;margin-top:14px}
  .post-text{font-size:12.3px;line-height:18.4px;color:var(--body);margin-top:12px;width:557px}
  .post-meta{display:flex;align-items:center;margin-top:16px;font-size:11.5px;color:var(--muted)}
  .post-meta span{display:flex;align-items:center;gap:7px}
  .post-meta svg{width:14px;height:14px}
  .meta-date{width:124px}.meta-comment{width:158px}.meta-like{width:103px}.meta-share{width:98px}
  .meta-more{margin-left:auto}

  .load-more{position:absolute;left:172px;top:2258px;width:557px;height:37px;background:var(--button-grey);display:flex;align-items:center;justify-content:center;gap:10px;font-size:12.5px;color:#333}

  .site-footer{position:absolute;left:0;top:2325px;width:1200px;height:40px;background:var(--purple);color:#fff;font-size:12px;text-align:center;line-height:40px}

  .widget{position:absolute;left:763px;width:265px;border:1px solid var(--panel-line);background:#fff}
  .widget-head{height:46px;background:linear-gradient(#fff,#ececec);display:flex;align-items:center;gap:10px;padding-left:16px;font-size:18px;color:#333}
  .widget-head svg{width:20px;height:20px}

  .search{top:561px;height:114px}
  .search-field{margin:16px 17px 0;height:33px;border:1px solid var(--panel-line);display:flex;align-items:center;justify-content:space-between;padding:0 10px;font-size:11px;font-style:italic;color:#999}

  .reviews{top:700px;height:303px}
  .reviews-head{height:70px;background:linear-gradient(#fff,#eeeeee);padding:8px 16px 0;position:relative}
  .reviews-for{font-size:11px;color:var(--green)}
  .reviews-brand{font-size:17px;font-weight:700;color:#333;line-height:20px}
  .reviews-arrows{position:absolute;right:12px;top:10px;font-size:15px;color:#888;letter-spacing:4px}
  .rating{display:flex;align-items:center;gap:6px;margin-top:5px}
  .rating svg{width:17px;height:17px}
  .rating em{font-style:normal;font-size:15px;color:var(--green);margin-left:3px;font-weight:700}
  .review{margin:0 16px;padding:6px 0 7px;border-bottom:1px solid var(--line);font-size:11.5px;line-height:18px;color:#333}
  .review a{display:block;color:var(--red);font-size:11.5px;text-decoration:none;margin-top:3px}
  .reviews-foot{display:flex;align-items:center;padding:8px 12px 0;font-size:12px;font-weight:700;color:var(--green)}
  .reviews-foot .partner{display:flex;align-items:center;gap:5px;font-size:17px;color:#333;font-weight:400;margin-right:auto}
  .reviews-foot .partner i{display:block;width:13px;height:13px;background:#333}
  .reviews-foot a{margin-left:26px;text-decoration:none;color:var(--green)}

  .social-feed{top:1028px;height:331px}
  .tabs{display:flex;height:38px;border-bottom:1px solid var(--panel-line)}
  .tabs span{flex:1;display:flex;align-items:center;justify-content:center;gap:5px;font-size:13px;color:#333;border-left:1px solid var(--panel-line);background:#f3f3f3}
  .tabs span:first-child{border-left:none;background:#fff}
  .tabs i{display:block;width:14px;height:14px;border:1px solid #777;border-radius:50%}
  .feed-item{display:flex;gap:9px;margin:14px 10px 0 10px;height:56px}
  .feed-thumb{width:52px;height:52px;flex:none;background:linear-gradient(135deg,#c69c7c,#4a2e2a)}
  .feed-text{font-size:11px;line-height:16px;color:#333}
  .like-btn{display:inline-flex;align-items:center;gap:3px;margin-top:3px;padding:0 4px;height:15px;border:1px solid #aab4c8;background:#eef1f7;font-size:9.5px;color:#3b5998;border-radius:2px}

  .archives{top:1389px;height:232px}
  .archives ul{list-style:none;margin:6px 16px 0}
  .archives li{height:35.5px;line-height:35px;border-bottom:1px solid var(--line);font-size:13px;color:#333;padding-left:16px;position:relative}
  .archives li:last-child{border-bottom:none}
  .archives li::before{content:"";position:absolute;left:0;top:16px;width:4px;height:4px;border-radius:50%;background:var(--red)}

  .newsletter{top:1648px;height:191px;padding:14px 16px}
  .newsletter p{font-size:16px;line-height:22px;color:#444}
  .email-field{margin-top:14px;height:33px;border:1px solid var(--panel-line);padding:0 10px;line-height:31px;font-size:11px;font-style:italic;color:#888}
  .delivery-btn{display:inline-block;margin-top:17px;width:90px;height:34px;line-height:34px;text-align:center;background:var(--purple);color:#fff;font-size:12px;font-weight:700}
</style>
</head>
<body>

<header class="site-header">
  <div class="brand">Marlowe Interiors</div>
  <nav class="social-links" aria-label="Social accounts">
    <a href="#" aria-label="Pagebook"></a>
    <a href="#" aria-label="Chirper"></a>
    <a href="#" aria-label="Snapgram"></a>
  </nav>
</header>

<section class="hero" role="img" aria-label="Photo of a bright white kitchen with granite island and pendant lanterns">
</section>
<div class="avatar" role="img" aria-label="Portrait of the designer"></div>
<div class="profile-name">MARLOWE</div>
<p class="profile-intro">Lorem ipsum dolor sit amet, consectetue adipiscing elit, sed diam nonum euismod tincidunt ut laoreet dolore magna...</p>

<article class="post" style="top:558px">
  <h2 class="post-title">Lorem ipsum dolor sit</h2>
  <p class="post-sub">Duis aute irure dolor in reprehenderit</p>
  <div class="post-image" role="img" aria-label="Dining table set with red gerbera centrepieces" style="background:linear-gradient(180deg,#7d86a0 0%,#9c8f9a 45%,#6a5560 70%,#b8b2b0 100%)"></div>
  <p class="post-text">Lorem ipsum dolor sit amet, consecit adipiscing elit, sed do eiusmod tempor incidimen labore n dolorme laboris ni ut aliquip ex ena lin consequat Duis aute irure dolor in reprehenderit magna aliqua. Ut enim ad qnexercitation ullamco Neque porro quisquam est, qui dolorem ipsum quia dolor sit amet, conadipi velit sed quia non numquam eius modi tempora incidunt. Quis autem vel eum iure reprimnderit in voluptate velit esse quam nihil molestiae consequatur.</p>
  <div class="post-meta">
    <span class="meta-date"><svg viewBox="0 0 14 14"><rect x="1" y="2" width="12" height="11" fill="none" stroke="#ec1f27" stroke-width="1.5"/><rect x="1" y="2" width="12" height="3" fill="#ec1f27"/></svg>19/03/2015</span>
    <span class="meta-comment"><svg viewBox="0 0 14 14"><ellipse cx="7" cy="6" rx="6.5" ry="5" fill="#ec1f27"/><path d="M3 9l-1 4 4-3z" fill="#ec1f27"/></svg>Leave A Comment</span>
    <span class="meta-like"><svg viewBox="0 0 14 14"><rect x="1" y="6" width="3" height="7" fill="#ec1f27"/><path d="M5 6l3-5c1 0 2 1 1.5 2.5L9 5.5h3.5c1 0 1.5 1 1 2l-1.5 5H5z" fill="#ec1f27"/></svg>Like Us</span>
    <span class="meta-share"><svg viewBox="0 0 14 14"><circle cx="11" cy="3" r="2.3" fill="#ec1f27"/><circle cx="3" cy="7" r="2.3" fill="#ec1f27"/><circle cx="11" cy="11" r="2.3" fill="#ec1f27"/><path d="M11 3L3 7l8 4" stroke="#ec1f27" stroke-width="1.4" fill="none"/></svg>Share</span>
    <span class="meta-more">Read More &nbsp;»</span>
  </div>
</article>

<article class="post" style="top:990px">
  <h2 class="post-title">Lorem ipsum dolor sit</h2>
  <p class="post-sub">Duis aute irure dolor in reprehenderit</p>
  <div class="post-image" role="img" aria-label="Modern white living space with open kitchen and bar stools" style="background:linear-gradient(90deg,#c9c3bb 0%,#efece7 25%,#8a6a4d 50%,#e8e4de 70%,#9a7a3a 100%)"></div>
  <p class="post-text">Lorem ipsum dolor sit amet, consecit adipiscing elit, sed do eiusmod tempor incidimen labore n dolorme laboris ni ut aliquip ex ena lin consequat Duis aute irure dolor in reprehenderit magna aliqua. Ut enim ad qnexercitation ullamco Neque porro quisquam est, qui dolorem ipsum quia dolor sit amet, conadipi velit sed quia non numquam eius modi tempora incidunt. Quis autem vel eum iure reprimnderit in voluptate velit esse quam nihil molestiae consequatur.</p>
  <div class="post-meta">
    <span class="meta-date"><svg viewBox="0 0 14 14"><rect x="1" y="2" width="12" height="11" fill="none" stroke="#ec1f27" stroke-width="1.5"/><rect x="1" y="2" width="12" height="3" fill="#ec1f27"/></svg>19/03/2015</span>
    <span class="meta-comment"><svg viewBox="0 0 14 14"><ellipse cx="7" cy="6" rx="6.5" ry="5" fill="#ec1f27"/><path d="M3 9l-1 4 4-3z" fill="#ec1f27"/></svg>Leave A Comment</span>
    <span class="meta-like"><svg viewBox="0 0 14 14"><rect x="1" y="6" width="3" height="7" fill="#ec1f27"/><path d="M5 6l3-5c1 0 2 1 1.5 2.5L9 5.5h3.5c1 0 1.5 1 1 2l-1.5 5H5z" fill="#ec1f27"/></svg>Like Us</span>
    <span class="meta-share"><svg viewBox="0 0 14 14"><circle cx="11" cy="3" r="2.3" fill="#ec1f27"/><circle cx="3" cy="7" r="2.3" fill="#ec1f27"/><circle cx="11" cy="11" r="2.3" fill="#ec1f27"/><path d="M11 3L3 7l8 4" stroke="#ec1f27" stroke-width="1.4" fill="none"/></svg>Share</span>
    <span class="meta-more">Read More &nbsp;»</span>
  </div>
</article>

<article class="post" style="top:1419px">
  <h2 class="post-title">Lorem ipsum dolor sit</h2>
  <p class="post-sub">Duis aute irure dolor in reprehenderit</p>
  <div class="post-image" role="img" aria-label="Loft living room with white sofa and red dining chairs" style="background:linear-gradient(180deg,#cfd3d2 0%,#e9e7e2 40%,#8c6e5a 75%,#8b2530 100%)"></div>
  <p class="post-text">Lorem ipsum dolor sit amet, consecit adipiscing elit, sed do eiusmod tempor incidimen labore n dolorme laboris ni ut aliquip ex ena lin consequat Duis aute irure dolor in reprehenderit magna aliqua. Ut enim ad qnexercitation ullamco Neque porro quisquam est, qui dolorem ipsum quia dolor sit amet, conadipi velit sed quia non numquam eius modi tempora incidunt. Quis autem vel eum iure reprimnderit in voluptate velit esse quam nihil molestiae consequatur.</p>
  <div class="post-meta">
    <span class="meta-date"><svg viewBox="0 0 14 14"><rect x="1" y="2" width="12" height="11" fill="none" stroke="#ec1f27" stroke-width="1.5"/><rect x="1" y="2" width="12" height="3" fill="#ec1f27"/></svg>19/03/2015</span>
    <span class="meta-comment"><svg viewBox="0 0 14 14"><ellipse cx="7" cy="6" rx="6.5" ry="5" fill="#ec1f27"/><path d="M3 9l-1 4 4-3z" fill="#ec1f27"/></svg>Leave A Comment</span>
    <span class="meta-like"><svg viewBox="0 0 14 14"><rect x="1" y="6" width="3" height="7" fill="#ec1f27"/><path d="M5 6l3-5c1 0 2 1 1.5 2.5L9 5.5h3.5c1 0 1.5 1 1 2l-1.5 5H5z" fill="#ec1f27"/></svg>Like Us</span>
    <span class="meta-share"><svg viewBox="0 0 14 14"><circle cx="11" cy="3" r="2.3" fill="#ec1f27"/><circle cx="3" cy="7" r="2.3" fill="#ec1f27"/><circle cx="11" cy="11" r="2.3" fill="#ec1f27"/><path d="M11 3L3 7l8 4" stroke="#ec1f27" stroke-width="1.4" fill="none"/></svg>Share</span>
    <span class="meta-more">Read More &nbsp;»</span>
  </div>
</article>

<article class="post" style="top:1849px">
  <h2 class="post-title">Lorem ipsum dolor sit</h2>
  <p class="post-sub">Duis aute irure dolor in reprehenderit</p>
  <div class="post-image" role="img" aria-label="Cream living room with gilded mirror and table lamps" style="background:linear-gradient(90deg,#5e4e44 0%,#d8cbb8 30%,#e9e1d4 60%,#c8b9a2 100%)"></div>
  <p class="post-text">Lorem ipsum dolor sit amet, consecit adipiscing elit, sed do eiusmod tempor incidimen labore n dolorme laboris ni ut aliquip ex ena lin consequat Duis aute irure dolor in reprehenderit magna aliqua. Ut enim ad qnexercitation ullamco Neque porro quisquam est, qui dolorem ipsum quia dolor sit amet, conadipi velit sed quia non numquam eius modi tempora incidunt. Quis autem vel eum iure reprimnderit in voluptate velit esse quam nihil molestiae consequatur.</p>
  <div class="post-meta">
    <span class="meta-date"><svg viewBox="0 0 14 14"><rect x="1" y="2" width="12" height="11" fill="none" stroke="#ec1f27" stroke-width="1.5"/><rect x="1" y="2" width="12" height="3" fill="#ec1f27"/></svg>19/03/2015</span>
    <span class="meta-comment"><svg viewBox="0 0 14 14"><ellipse cx="7" cy="6" rx="6.5" ry="5" fill="#ec1f27"/><path d="M3 9l-1 4 4-3z" fill="#ec1f27"/></svg>Leave A Comment</span>
    <span class="meta-like"><svg viewBox="0 0 14 14"><rect x="1" y="6" width="3" height="7" fill="#ec1f27"/><path d="M5 6l3-5c1 0 2 1 1.5 2.5L9 5.5h3.5c1 0 1.5 1 1 2l-1.5 5H5z" fill="#ec1f27"/></svg>Like Us</span>
    <span class="meta-share"><svg viewBox="0 0 14 14"><circle cx="11" cy="3" r="2.3" fill="#ec1f27"/><circle cx="3" cy="7" r="2.3" fill="#ec1f27"/><circle cx="11" cy="11" r="2.3" fill="#ec1f27"/><path d="M11 3L3 7l8 4" stroke="#ec1f27" stroke-width="1.4" fill="none"/></svg>Share</span>
    <span class="meta-more">Read More &nbsp;»</span>
  </div>
</article>

<div class="load-more">
  <svg width="16" height="16" viewBox="0 0 16 16"><circle cx="8" cy="8" r="5.5" fill="none" stroke="#9a9a9a" stroke-width="2" stroke-dasharray="3 2"/></svg>
  Load more blog
</div>

<aside>
  <section class="widget search">
    <div class="widget-head">
      <svg viewBox="0 0 20 20"><circle cx="4" cy="16" r="2.5" fill="#e54d9c"/><path d="M2 9a9 9 0 0 1 9 9M2 3a15 15 0 0 1 15 15" fill="none" stroke="#e54d9c" stroke-width="2.4"/></svg>
      Search Blog
    </div>
    <div class="search-field">Search...
      <svg width="12" height="12" viewBox="0 0 12 12"><circle cx="5" cy="5" r="3.8" fill="none" stroke="#aaa" stroke-width="1.3"/><path d="M8 8l3 3" stroke="#aaa" stroke-width="1.3"/></svg>
    </div>
  </section>

  <section class="widget reviews">
    <div class="reviews-head">
      <div class="reviews-for">Reviews For</div>
      <div class="reviews-brand">Marlowe Interiors</div>
      <div class="reviews-arrows">‹›</div>
      <div class="rating">
        <svg viewBox="0 0 20 20"><path d="M10 1l2.7 6 6.3.6-4.8 4.3 1.4 6.4L10 15l-5.6 3.3 1.4-6.4L1 7.6l6.3-.6z" fill="#ec1f27"/></svg>
        <svg viewBox="0 0 20 20"><path d="M10 1l2.7 6 6.3.6-4.8 4.3 1.4 6.4L10 15l-5.6 3.3 1.4-6.4L1 7.6l6.3-.6z" fill="#ec1f27"/></svg>
        <svg viewBox="0 0 20 20"><path d="M10 1l2.7 6 6.3.6-4.8 4.3 1.4 6.4L10 15l-5.6 3.3 1.4-6.4L1 7.6l6.3-.6z" fill="#ec1f27"/></svg>
        <svg viewBox="0 0 20 20"><path d="M10 1l2.7 6 6.3.6-4.8 4.3 1.4 6.4L10 15l-5.6 3.3 1.4-6.4L1 7.6l6.3-.6z" fill="#ec1f27"/></svg>
        <svg viewBox="0 0 20 20"><path d="M10 1l2.7 6 6.3.6-4.8 4.3 1.4 6.4L10 15l-5.6 3.3 1.4-6.4L1 7.6l6.3-.6z" fill="#333"/></svg>
        <em>See all reviews</em>
      </div>
    </div>
    <div class="review">Lorem ipsum dolor sit amet, consectetuer adipiscing elit, sed diam nonummy nibh<a href="#">Read More</a></div>
    <div class="review">Lorem ipsum dolor sit amet, consectetuer adipiscing elit, sed diam nonummy nibh<a href="#">Read More</a></div>
    <div class="review">Lorem ipsum dolor sit amet, consectetuer<a href="#">Read More</a></div>
    <div class="reviews-foot">
      <span class="partner"><i></i>Nestly</span>
      <a href="#">All Reviews</a>
      <a href="#">Reviews Me</a>
    </div>
  </section>

  <section class="widget social-feed">
    <div class="tabs">
      <span><i></i>Pagebook</span>
      <span><i></i>Chirper</span>
      <span><i></i>Snapgram</span>
    </div>
    <div class="feed-item"><div class="feed-thumb" role="img" aria-label="Follower profile photo"></div><div class="feed-text">Lorem Ipsum is simply dummy text of the, printing and typesetting...<br><span class="like-btn">▲ Like</span></div></div>
    <div class="feed-item"><div class="feed-thumb" role="img" aria-label="Follower profile photo"></div><div class="feed-text">Lorem Ipsum is simply dummy text of the, printing and typesetting...<br><span class="like-btn">▲ Like</span></div></div>
    <div class="feed-item"><div class="feed-thumb" role="img" aria-label="Follower profile photo" style="background:linear-gradient(135deg,#f2f2f2,#7a5a48)"></div><div class="feed-text">Lorem Ipsum is simply dummy text of the, printing and typesetting...<br><span class="like-btn">▲ Like</span></div></div>
    <div class="feed-item"><div class="feed-thumb" role="img" aria-label="Follower profile photo"></div><div class="feed-text">Lorem Ipsum is simply dummy text of the, printing and typesetting...<br><span class="like-btn">▲ Like</span></div></div>
  </section>

  <section class="widget archives">
    <div class="widget-head">
      <svg viewBox="0 0 20 20"><path d="M4 1h8l4 4v14H4z" fill="none" stroke="#e54d9c" stroke-width="1.8"/><path d="M10 8v6M7.5 11.5L10 14l2.5-2.5" fill="none" stroke="#e54d9c" stroke-width="1.6"/></svg>
      Archives
    </div>
    <ul>
      <li>March 2015</li>
      <li>Feb 2015</li>
      <li>Jan 2015</li>
      <li>December 2014</li>
      <li>November 2014</li>
    </ul>
  </section>

  <section class="widget newsletter">
    <p>Sing Up To Get Exclusive Offers From Our Favorite Brands And To Be Well Up In The News.</p>
    <div class="email-field">Enter your email address</div>
    <span class="delivery-btn">DELIVERY</span>
  </section>
</aside>

<footer class="site-footer">Copyright © 2015 MarloweInteriors. All rights reserved.</footer>

</body>
</html>
```